We specialize in pizza, pasta and salads and are now offering TAKE & BAKE and GRAB & GO ...

Looking for either a 8.5" x 11" or similar for a instore display. WILL BE ON A SWIVELING HOLDER to catch customers attention.

**THIS IS A DOUBLE SIDED PRINT**

ONE SIDE will consist of WHAT'S FOR DINNER TONIGHT? and the following:
* Take & Bake"
* "Baked Pasta"
* Freshly made in house
* Lasagna
$13.50
- please include attached closeup picture and logo

THE OTHER SIDE will consist of
mini charcutier board.
* snack size charcutier delight *
* Enjoy the flavors of gourmet snacking, all in one convenient box!

PRICE $8.99

Winning design will be commissioned to design labels for "grab and go" for take and bake pasta, charcuterie box, pasta salads, candy etc.

Thank you and please do not hesitate to ask any questions.

www.belmaropizza.ca
www.peachnook.ca
Logo to be interchanged as they are affiliated meaning PeachNook is a brand within Belmaro pizza.

our target market is customers who have already entered our business. This is to upsel

We are in a self serve enviroment and target business people

• must be clean and catchy. We are located in a professional business community.
• Must be appealing, appetizing and utilize our website colors
• should not have any carton drawings and not be cluttered (busy)

```html
<!DOCTYPE html>
<html lang="en">
<head>
<meta charset="utf-8">
<title>Belmaro Pizza – Take &amp; Bake and Grab &amp; Go Display</title>
<link rel="stylesheet" href="https://fonts.googleapis.com/css2?family=Bebas+Neue&family=Kalam:wght@400&family=Oswald:wght@200;300;400&display=swap">
<style>
  :root {
    --red: #b0282f;
    --navy: #1c1d3b;
    --white: #ffffff;
    --paper: #ffffff;
    --photo-light: #eadcbc;
    --photo-mid: #c08a45;
    --photo-dark: #5e3f22;
  }
  * { box-sizing: border-box; margin: 0; padding: 0; }
  html, body {
    width: 1200px; height: 816px; overflow: hidden;
    background: var(--paper);
  }
  .spread { position: relative; width: 1200px; height: 816px; }
  .flyer {
    position: absolute; top: 36px;
    width: 574px; height: 744px;
    overflow: hidden;
    background: var(--navy);
    box-shadow: 0 1px 4px rgba(0,0,0,0.25);
  }
  .flyer--dinner { left: 13px; }
  .flyer--charcuterie { left: 611px; }
  .flyer__shapes { position: absolute; inset: 0; width: 574px; height: 744px; }
  .flyer__photo {
    position: absolute; left: -12px; top: -14px;
    width: 264px; height: 264px; border-radius: 50%;
    background:
      radial-gradient(circle at 45% 30%, var(--photo-light) 0%, var(--photo-mid) 45%, var(--photo-dark) 100%);
  }
  .flyer__title {
    position: absolute; right: 19px; top: 60px;
    font-family: "Bebas Neue", sans-serif; font-weight: 400;
    font-size: 54px; line-height: 45px; letter-spacing: 1px;
    color: var(--white); text-align: right;
  }
  .flyer__list {
    position: absolute; list-style: none;
    font-family: "Oswald", sans-serif; font-weight: 200;
    color: var(--white); text-transform: uppercase;
  }
  .flyer--dinner .flyer__list {
    left: 90px; top: 300px; font-size: 42px; line-height: 63px;
  }
  .flyer--charcuterie .flyer__list {
    left: 79px; top: 336px; font-size: 32px; line-height: 47.5px;
  }
  .flyer__list .indent { padding-left: 17px; display: block; }
  .flyer__price {
    position: absolute; left: 410px; top: 544px; width: 176px;
    font-family: "Bebas Neue", sans-serif;
    font-size: 60px; line-height: 60px; letter-spacing: 1px;
    color: var(--white); text-align: center;
  }
  .flyer__tagline {
    position: absolute; left: 38px; top: 586px;
    font-family: "Kalam", cursive;
    font-size: 17px; line-height: 17px;
    color: var(--white); white-space: nowrap;
  }
  .brand {
    position: absolute;
    display: flex; align-items: center; gap: 6px;
    font-family: "Oswald", sans-serif; font-weight: 400;
    color: var(--navy); white-space: nowrap;
  }
  .brand--catering { left: 19px; top: 665px; height: 62px; font-size: 28px; line-height: 34px; }
  .brand__dot {
    flex: none;
    width: 62px; height: 62px; border-radius: 50%;
    border: 2px solid var(--navy);
  }
  .brand--pizza { left: 302px; top: 673px; font-size: 40px; line-height: 48px; font-weight: 300; letter-spacing: 1px; }
  .flyer__address {
    position: absolute; left: 0; right: 0; top: 721px;
    font-family: "Oswald", sans-serif; font-weight: 400;
    font-size: 14px; line-height: 18px; color: var(--navy); text-align: center;
    white-space: nowrap;
  }
</style>
</head>
<body>
<main class="spread">

  <section class="flyer flyer--dinner">
    <svg class="flyer__shapes" viewBox="0 0 574 744" aria-hidden="true">
      <rect width="574" height="744" fill="var(--navy)"/>
      <path fill="var(--red)" d="M0 0 H574 V205 L558 212 L540 200 L520 210 L498 194 L478 204 L456 189 L436 197 L414 180 L398 188 L382 170 L366 181 L350 172 L334 186 L318 176 L300 166 L284 178 L268 190 L250 202 L230 232 L200 278 L0 300 Z"/>
      <circle cx="120" cy="128" r="146" fill="var(--red)"/>
      <polygon fill="var(--red)" points="0,635 574,625 574,640 0,653"/>
      <polygon fill="var(--white)" points="0,659 574,646 574,744 0,744"/>
      <circle cx="498" cy="573" r="88" fill="var(--red)"/>
    </svg>
    <div class="flyer__photo" role="img" aria-label="Close-up photo of baked pasta with stretching melted cheese"></div>
    <h1 class="flyer__title">Dinner Tonight</h1>
    <ul class="flyer__list">
      <li>* Take &amp; Bake"</li>
      <li>* "Baked Pasta"</li>
      <li>* Freshly made in house</li>
      <li>* Lasagna</li>
    </ul>
    <p class="flyer__price">$13.50</p>
    <p class="flyer__tagline">We specialize in pizza, pasta and salads and are<br>now offering TAKE &amp; BAKE and GRAB &amp; GO</p>
    <div class="brand brand--catering"><span class="brand__dot"></span><span>PeachNook</span></div>
    <div class="brand brand--pizza">BELMARO PIZZA</div>
    <p class="flyer__address">HARBOR POINT PLAZA 318, 410 7 AVENUE SW</p>
  </section>

  <section class="flyer flyer--charcuterie">
    <svg class="flyer__shapes" viewBox="0 0 574 744" aria-hidden="true">
      <rect width="574" height="744" fill="var(--navy)"/>
      <path fill="var(--red)" d="M0 0 H574 V205 L558 212 L540 200 L520 210 L498 194 L478 204 L456 189 L436 197 L414 180 L398 188 L382 170 L366 181 L350 172 L334 186 L318 176 L300 166 L284 178 L268 190 L250 202 L230 232 L200 278 L0 300 Z"/>
      <circle cx="120" cy="128" r="146" fill="var(--red)"/>
      <polygon fill="var(--red)" points="0,635 574,625 574,640 0,653"/>
      <polygon fill="var(--white)" points="0,659 574,646 574,744 0,744"/>
      <circle cx="498" cy="573" r="88" fill="var(--red)"/>
    </svg>
    <div class="flyer__photo" role="img" aria-label="Close-up photo of baked pasta with stretching melted cheese"></div>
    <h1 class="flyer__title">Mini Charcutier<br>Board</h1>
    <ul class="flyer__list">
      <li>* Snack size charcutier delight *</li>
      <li>* Enjoy the flavors of gourmet
        <span class="indent">snacking, all in one</span>
        <span class="indent">convenient box!</span></li>
    </ul>
    <p class="flyer__price">$8.99</p>
    <p class="flyer__tagline">We specialize in pizza, pasta and salads and are<br>now offering TAKE &amp; BAKE and GRAB &amp; GO</p>
    <div class="brand brand--catering"><span class="brand__dot"></span><span>PeachNook</span></div>
    <div class="brand brand--pizza">BELMARO PIZZA</div>
    <p class="flyer__address">HARBOR POINT PLAZA 318, 410 7 AVENUE SW</p>
  </section>

</main>
</body>
</html>
```